Political sign design, fonts colors and layout

I am running for Town Council.

My message is done, and *a draft is attached* with the text we wish to use. It says "Elect Dana Velmont" etc. In Maroon and White. I am not a designer, but this is somewhat close to what we are looking for.

I need help with colors and fonts, layout, spacing, and general cleanup.

I'm attaching the town high school logo:

- "H" for Brookfield: with black and white outlines on the fonts
- we want to incorporate the black and white on the fonts
- for the entire text, parts of the text, or best would be a mix

This is for signs printed and placed all over my town.

We need two versions

1. square, 4' by 4' version
2. 36" by 24" version

The smaller version will drop the three bullet pointed text, but otherwise can be identical.

The sign can only use 3 printed colors (due to printing costs.)

1. maroon,
2. white,
3. black.

The maroon should match the maroon from the high school logo attached, which I believe I did in the draft.

We also like the white border around the outside, like in the "scoreboard" design attached.

Thanks for your attention, wish me luck.

Dana

Target Market(s)

SIgns, Political market

Industry/Entity Type

Political

Font styles to use
Sans Serif
Other font styles liked:
• Arial Black, Sans Serif Bold

Requirements
Must have
• maroon background, white font.
• - black borders around fonts where appropriate
• - great spacing
• - great typeface usage
• - clean and crisp political sign, visible while driving.
• - my name "Dana Velmont" much larger like the draft, or the appropriate additional size
• - two versions, one square, and one 36" / 24"
Nice to have
• - nice borders
• - dress it up a bit, using italics and bold fonts, without making it flashy or busy.
Should not have
• Must be easily readable from a car, except for "Paid for by Friends of Dana Velmont" which can be tiny.
• Colors are noted in the description, the "Brookfield Maroon" as the background, white font, and some use of black.

```html
<!DOCTYPE html>
<html lang="en">
<head>
<meta charset="utf-8">
<title>Elect Dana Velmont – Brookfield Town Council Sign</title>
<link rel="stylesheet" href="https://fonts.googleapis.com/css2?family=Archivo:ital,wght@0,700;0,800;0,900;1,700;1,800;1,900&family=Roboto+Condensed:wght@700;800;900&display=swap">
<style>
  :root {
    --brookfield-maroon: #761c2e;
    --sign-white: #ffffff;
    --ink-black: #2b2b2b;
    --shadow-black: #2a2a2a;
  }
  html, body {
    margin: 0;
    padding: 0;
    overflow: hidden;
    background: var(--brookfield-maroon);
  }
  .sign {
    position: relative;
    width: 800px;
    height: 1200px;
    background: var(--brookfield-maroon);
    overflow: hidden;
    font-family: "Archivo", Arial, sans-serif;
  }
  .frame {
    position: absolute;
    box-sizing: border-box;
    border: 10px solid var(--sign-white);
  }
  .frame--header { left: 16px; top: 16px; width: 766px; height: 429px; }
  .frame--footer { left: 18px; top: 1012px; width: 764px; height: 170px; }

  .slogan {
    position: absolute;
    left: 0; top: 48px; width: 800px;
    margin: 0;
    text-align: center;
    font-family: "Roboto Condensed", "Arial Narrow", sans-serif;
    font-weight: 800;
    font-size: 80px;
    line-height: 1;
    letter-spacing: 1px;
    color: var(--sign-white);
    text-shadow: -3px 3px 0 var(--shadow-black);
  }
  .elect {
    position: absolute;
    left: 0; top: 166px; width: 800px;
    text-align: center;
    font-weight: 900;
    font-size: 31px;
    line-height: 1;
    color: var(--sign-white);
    text-shadow: -2px 2px 0 var(--shadow-black);
  }
  .fitted { position: absolute; overflow: visible; }
  .candidate-name { left: 40px; top: 210px; }
  .fitted text {
    font-family: "Roboto Condensed", "Arial Narrow", sans-serif;
    font-weight: 800;
  }
  .office {
    position: absolute;
    right: 44px; top: 377px;
    font-style: italic;
    font-weight: 800;
    font-size: 27px;
    line-height: 1;
    color: var(--sign-white);
  }

  .platform {
    position: absolute;
    left: 24px; top: 470px;
    width: 750px; height: 517px;
    background: var(--sign-white);
  }
  .platform__lead {
    position: absolute;
    left: 0; top: 42px; width: 750px;
    text-align: center;
    font-weight: 800;
    font-size: 43px;
    line-height: 1;
    color: var(--ink-black);
  }
  .town-name { left: 76px; top: 120px; }
  .town-name text {
    font-family: "Archivo", Arial, sans-serif;
    font-weight: 900;
  }
  .platform__url {
    position: absolute;
    left: 0; top: 228px; width: 750px;
    text-align: center;
    font-weight: 900;
    font-size: 44px;
    line-height: 1;
    color: var(--ink-black);
  }
  .issues {
    position: absolute;
    left: 64px; top: 330px;
    margin: 0; padding: 0;
    list-style: none;
  }
  .issues li {
    position: relative;
    padding-left: 34px;
    height: 55px;
    font-style: italic;
    font-weight: 900;
    font-size: 37px;
    line-height: 44px;
    letter-spacing: 0.5px;
    color: var(--ink-black);
  }
  .issues li::before {
    content: "";
    position: absolute;
    left: 0; top: 16px;
    width: 16px; height: 16px;
    border-radius: 50%;
    background: var(--brookfield-maroon);
  }

  .vote-call { left: 44px; top: 1040px; }
  .disclaimer {
    position: absolute;
    left: 0; top: 1142px; width: 800px;
    text-align: center;
    font-style: italic;
    font-weight: 700;
    font-size: 19px;
    line-height: 1;
    color: var(--sign-white);
  }
</style>
</head>
<body>
<main class="sign">
  <div class="frame frame--header"></div>

  <h1 class="slogan">Take back our Town!</h1>
  <div class="elect">Elect</div>

  <svg class="fitted candidate-name" width="720" height="160" viewBox="0 0 720 160" aria-label="Dana Velmont">
    <text x="354" y="148" font-size="174" textLength="704" lengthAdjust="spacingAndGlyphs" text-anchor="middle" fill="var(--shadow-black)">DANA VELMONT</text>
    <text x="360" y="142" font-size="174" textLength="704" lengthAdjust="spacingAndGlyphs" text-anchor="middle" fill="var(--sign-white)">DANA VELMONT</text>
  </svg>

  <div class="office">for Brookfield Councilman / Trustee</div>

  <section class="platform">
    <div class="platform__lead">Fighting for</div>
    <svg class="fitted town-name" width="600" height="80" viewBox="0 0 600 80" aria-label="Brookfield">
      <text x="300" y="70" font-size="84" textLength="590" lengthAdjust="spacingAndGlyphs" text-anchor="middle"
            fill="var(--brookfield-maroon)" stroke="var(--ink-black)" stroke-width="9" stroke-linejoin="round">BROOKFIELD</text>
      <text x="300" y="70" font-size="84" textLength="590" lengthAdjust="spacingAndGlyphs" text-anchor="middle"
            fill="var(--brookfield-maroon)" stroke="var(--sign-white)" stroke-width="4" stroke-linejoin="round">BROOKFIELD</text>
      <text x="300" y="70" font-size="84" textLength="590" lengthAdjust="spacingAndGlyphs" text-anchor="middle"
            fill="var(--brookfield-maroon)">BROOKFIELD</text>
    </svg>
    <div class="platform__url">www.brookfieldfirst.org</div>
    <ul class="issues">
      <li>Stop HIGH taxes</li>
      <li>Clean up our government</li>
      <li>Preserve our Neighborhoods</li>
    </ul>
  </section>

  <div class="frame frame--footer"></div>
  <svg class="fitted vote-call" width="716" height="90" viewBox="0 0 716 90" aria-label="Vote Nov. 8th, Row A">
    <text x="355" y="82" font-size="92" textLength="704" lengthAdjust="spacingAndGlyphs" text-anchor="middle" fill="var(--shadow-black)">Vote Nov. 8th «Row A»</text>
    <text x="358" y="79" font-size="92" textLength="704" lengthAdjust="spacingAndGlyphs" text-anchor="middle" fill="var(--sign-white)">Vote Nov. 8th «Row A»</text>
  </svg>
  <div class="disclaimer">Paid for by Friends of Dana</div>
</main>
</body>
</html>
```